Not another boring Business Card Design Project

This is not another boring Business Card Design Project.

We are looking for the weirdest, wackiest most boundary pushing designs that you can come up with.

If you believe that design can be fun, energetic, crazy, unpredictable, beautiful and eye-catching then read on… this project is for you.

We are Tolvin Presk and we print plastic cards.

We are running a Plastic Card Design Competition.

And we need a plastic card to advertise the competition to graphic designers just like you.

The design needs to make your average designers’ jaws drop and their eyes pop out.

You can do what you wish with the card design, so long as it stands out.

We like these designs, designs that stretch the boundaries and become something beyond just another business card:

http://quorvamedia.net/wp-content/uploads/2009/03/b48.jpg
Designer - http://www.pelvanworks.com/

http://quorvamedia.net/wp-content/uploads/2009/03/b41.jpg
Designer - http://renolbrakstad.com/

http://images.plinthhive.com/designs/44195_732292_37774_thumbnail.jpg
Designer- Zentro Media at Plinth Hive

http://images.plinthhive.com/designs/44195_717529_37774_thumbnail.jpg
Designer - Zentro Media at Plinth Hive

http://quorvamedia.net/wp-content/uploads/2009/03/b11.jpg
Designer - http://www.wk7studio.com/

http://quorvamedia.net/wp-content/uploads/2009/03/b16.jpg
Designer - http://www.pebbletumbler.com/

Reason: A number of designers have said they want to submit designs and haven't yet done so, we want to give them time.

Reason: We've extended the deadline by 4 days for those who want to submit their designs over the weekend and give ourselves time to judge them

Plastic

• The design needs to contain this link: lnk.example/QzRpLk and any other detail that will encourage competition entry. The design will be printed on plastic.
• No borders (when plastic cards are punched to shape and size there is movement of 1 - 2mm, borders highlight this movement).

Keep text 3mm away from edges of the cards.

Please don't create designs to be produced on clear/transparent plastic.

```html
<!DOCTYPE html>
<html lang="en">
<head>
<meta charset="utf-8">
<title>Plastic Card Design Competition</title>
<link rel="stylesheet" href="https://fonts.googleapis.com/css2?family=Tinos:wght@400&display=swap">
<style>
  :root {
    --page-bg: #ffffff;
    --card-dark: #14180f;
    --card-mid: #252617;
    --card-warm: #3a3220;
    --title-light: #d7772c;
    --title-deep: #8a3d16;
    --link-colour: #d0602a;
  }
  html, body {
    margin: 0;
    padding: 0;
    width: 1200px;
    height: 851px;
    overflow: hidden;
    background: var(--page-bg);
  }
  .canvas {
    position: relative;
    width: 1200px;
    height: 851px;
  }
  .promo-card {
    position: absolute;
    left: 50px;
    top: 78px;
    width: 1100px;
    height: 694px;
    border-radius: 40px;
    overflow: hidden;
  }
  .promo-card svg {
    display: block;
    width: 100%;
    height: 100%;
  }
  .card-title {
    font-family: "Tinos", "Times New Roman", serif;
    font-size: 112px;
    fill: url(#titleFill);
  }
  .card-link {
    font-family: "Tinos", "Times New Roman", serif;
    font-size: 28px;
    font-weight: 700;
    fill: var(--link-colour);
  }
</style>
</head>
<body>
<main class="canvas">
  <section class="promo-card">
    <svg viewBox="0 0 1100 694" xmlns="http://www.w3.org/2000/svg">
      <defs>
        <radialGradient id="woodTone" cx="0.6" cy="0.25" r="0.85">
          <stop offset="0" stop-color="var(--card-warm)"/>
          <stop offset="0.5" stop-color="var(--card-mid)"/>
          <stop offset="1" stop-color="var(--card-dark)"/>
        </radialGradient>
        <linearGradient id="titleFill" x1="0" y1="0" x2="0" y2="1">
          <stop offset="0" stop-color="var(--title-light)"/>
          <stop offset="1" stop-color="var(--title-deep)"/>
        </linearGradient>
      </defs>

      <rect class="card-background" width="1100" height="694" fill="url(#woodTone)"
            role="img" aria-label="Dark weathered wooden boards texture"/>

      <g class="card-headline">
        <text class="card-title" x="80" y="245" textLength="963" lengthAdjust="spacingAndGlyphs">PLASTIC CARD</text>
        <text class="card-title" x="550" y="407" textLength="493" lengthAdjust="spacingAndGlyphs">DESIGN</text>
        <text class="card-title" x="69" y="565" textLength="974" lengthAdjust="spacingAndGlyphs">COMPETITION</text>
      </g>

      <text class="card-link" x="1039" y="613" text-anchor="end">lnk.example/QzRpLk</text>
    </svg>
  </section>
</main>
</body>
</html>
```